Trifold flyer for our dental clinic (the Bright Harbor Clinic)

The goal of this project is to design a trifold flyer for our dental clinic (the Bright Harbor Clinic). The winning design is expected to be creative, artistic and coherent with our logo.
Updates

Designs look the same

Target Market(s)

Young generation with dental need.

Industry/Entity Type

Dental Clinic

Font styles to use
Sans Serif

Colors
0355a3
85acd3
85cae6
0592cd
00a990
86cfc6
cedeed
cee9f5
cfeae6

Requirements
Must have
• See the attached sketch for content arrangement.

```html
<!DOCTYPE html>
<html lang="en">
<head>
<meta charset="utf-8">
<title>Bright Harbor Clinic – Trifold Flyer</title>
<link href="https://fonts.googleapis.com/css2?family=Montserrat:wght@400;600;700;800&family=Open+Sans:ital,wght@0,400;0,600;0,700;1,400&display=swap" rel="stylesheet">
<style>
:root{
  --navy:#0355a3;--sky:#85acd3;--aqua:#85cae6;--blue:#0592cd;--teal:#00a990;
  --mint:#86cfc6;--pale:#cedeed;--ice:#cee9f5;--foam:#cfeae6;--ink:#1d2b3a;--white:#fff;--alert:#e0282e;
}
*{box-sizing:border-box;margin:0;padding:0}
html,body{width:793px;height:1200px;overflow:hidden;background:#f3f5f8}
body{font-family:"Open Sans",sans-serif;color:var(--ink);position:relative}
.row-label{position:absolute;left:0;width:793px;text-align:center;font:700 22px "Montserrat",sans-serif;color:var(--ink)}
.sheet{position:absolute;left:8px;width:777px;display:flex;background:var(--white);box-shadow:0 1px 4px rgba(0,0,0,.15)}
.panel{width:259px;height:100%;position:relative;overflow:hidden;padding:12px}
.panel+.panel{border-left:1px solid #e2e8ee}
.ph{border-radius:4px}
h2{font:800 16px "Montserrat",sans-serif;color:var(--navy);text-transform:uppercase}
h2.light{text-transform:none;font-weight:700;font-size:17px}
/* meet us */
.doc{display:flex;align-items:center;gap:10px;margin-top:8px}
.doc .ph{width:44px;height:44px;background:linear-gradient(#7a8a9c,#3d4c5c);flex:none}
.doc b{display:block;font:700 10px "Montserrat",sans-serif;color:var(--navy);margin-bottom:2px}
.doc small{display:block;font-size:8.5px;line-height:1.3;color:var(--teal)}
.reviews{margin-top:12px;background:var(--navy);color:var(--white);padding:10px;height:306px}
.reviews h2{color:var(--white);text-align:center;font-size:14px;margin-bottom:6px}
.quote{background:var(--white);color:var(--ink);font-size:8.5px;padding:7px 8px;margin-bottom:8px;line-height:1.4}
.quote i{display:block}
.quote b{display:block;text-align:right;font-size:7.5px;color:var(--navy)}
/* hours panel */
.hero{height:170px;margin:-12px -12px 0;background:linear-gradient(120deg,var(--ice),var(--aqua) 70%,var(--sky));position:relative}
.hours{position:absolute;right:14px;top:58px;text-align:center;width:130px}
.hours strong{display:block;font:800 12px "Montserrat",sans-serif;color:var(--navy);line-height:1.2}
.hours span{display:block;font-size:8px;margin-top:3px}
.call{text-align:center;margin-top:8px;font-size:9px}
.call strong{display:block;font:800 22px "Montserrat",sans-serif;color:var(--navy)}
.address{border:2px solid var(--navy);margin:8px 20px;text-align:center;padding:6px;font-size:11px;line-height:1.35}
.address b{display:block;font:800 12px "Montserrat",sans-serif;color:var(--navy);text-decoration:underline}
.map-title{text-align:center;background:var(--navy);color:var(--white);font:700 12px "Montserrat",sans-serif;padding:4px}
.map{height:150px;background:linear-gradient(135deg,#e8ecef,#d4dde3)}
.web{text-align:center;font-size:8px;margin-top:5px;color:var(--navy)}
/* cover panel */
.brand-tile{position:absolute;right:12px;top:12px;width:130px;height:92px;background:var(--ice);display:flex;flex-direction:column;align-items:center;justify-content:center;gap:6px;padding:0 6px}
.brand-tile i{width:34px;height:34px;border-radius:50%;background:var(--blue);flex:none}
.brand-tile span{font:700 11px "Montserrat",sans-serif;color:var(--blue);text-transform:uppercase;text-align:center;line-height:1.2}
.collage{position:absolute;left:12px;top:110px;width:235px;height:200px;background:linear-gradient(135deg,#e7b3a8,#f4d9cf 50%,#d99b8e)}
.collage-top{position:absolute;left:12px;top:12px;width:104px;height:92px;background:linear-gradient(135deg,#f0cbc1,#d8988a)}
.offer{position:absolute;left:12px;right:12px;top:325px}
.offer h2{text-align:right;font-size:17px;margin-bottom:8px}
.deal{display:flex;height:40px;margin-bottom:8px}
.deal .price{width:68px;background:var(--teal);color:var(--white);font:800 26px "Montserrat",sans-serif;display:flex;align-items:center;justify-content:center;flex:none}
.deal .what{flex:1;min-width:0;border:2px solid var(--teal);display:flex;align-items:center;padding-left:8px;font:700 11px "Montserrat",sans-serif}
.deal.navy .price{background:var(--navy)}.deal.navy .what{border-color:var(--navy)}
.offer p{text-align:right;font:700 10px "Montserrat",sans-serif;color:var(--teal)}
/* R2 */
.promo .deal{height:44px}
.promo .deal .what{font-size:9px;line-height:1.25;flex-direction:column;align-items:flex-start;justify-content:center}
.promo .deal .what small{font-weight:400;color:var(--alert);font-size:7.5px}
.promo-note{font:800 10px "Montserrat",sans-serif;color:var(--alert);line-height:1.3}
.services h2{margin:12px 0 6px}
.svc{display:flex;align-items:center;gap:8px;margin-bottom:6px}
.svc .ph{width:60px;height:50px;background:linear-gradient(135deg,var(--pale),var(--sky));flex:none}
.svc span{flex:1;background:var(--ice);font:700 11px "Montserrat",sans-serif;padding:8px;color:var(--navy)}
.teeth{height:170px;margin:0 10px;background:radial-gradient(circle at 50% 55%,var(--white) 30%,var(--ice) 70%)}
.checks{list-style:none;margin:14px 6px}
.checks li{display:flex;align-items:center;gap:8px;font:600 11px "Montserrat",sans-serif;margin-bottom:12px}
.checks svg{flex:none}
.plan{text-align:center;font:800 19px "Montserrat",sans-serif;color:var(--navy);line-height:1.2;margin-top:24px}
.tier{display:flex;gap:8px;margin-bottom:10px}
.tier .ph{width:120px;height:86px;background:linear-gradient(135deg,var(--pale),#8aa2b8);flex:none}
.tier .pct{flex:1;text-align:center;font:800 15px "Montserrat",sans-serif;color:var(--navy);line-height:1.3;padding-top:12px}
.tier .pct small{display:block;font-size:11px;font-weight:600}
.tier-cap{font-size:8px;margin:-7px 0 9px;width:130px}
.fee{position:absolute;right:12px;bottom:16px;width:110px;text-align:center;font:800 14px "Montserrat",sans-serif;color:var(--navy);line-height:1.25}
</style>
</head>
<body>
<div class="row-label" style="top:2px">R1</div>
<section class="sheet" style="top:32px;height:560px">
  <div class="panel">
    <h2 class="light">Meet us</h2>
    <div class="doc"><div class="ph" role="img" aria-label="Portrait of Dr. Nora Wells"></div><div><b>NORA WELLS, DMD, MS</b><small>Board Certified Orthodontist</small></div></div>
    <div class="doc"><div class="ph" role="img" aria-label="Portrait of Dr. Peter L. Crane"></div><div><b>PETER L. CRANE, DMD</b><small>Board Certified Pediatric Dentist</small><small>Board Certified Orthodontist</small></div></div>
    <div class="doc"><div class="ph" role="img" aria-label="Portrait of Dr. Lina Moreau"></div><div><b>DR. LINA MOREAU, DMD</b><small>General Dentist</small></div></div>
    <div class="reviews">
      <h2>Reviews</h2>
      <div class="quote"><i>"Great care from the whole team. The doctor explained every step and the staff made our kids feel at home. We will be back."</i><b>CAROL BENTON<br>3/10/2018</b></div>
      <div class="quote"><i>"Best in town! Quick visits, gentle hands and a bright new smile."</i><b>VICTOR ELLISON<br>3/10/2018</b></div>
      <div class="quote"><i>"Great service. Everyone was so friendly!"</i><b>OWEN MARSH<br>3/10/2018</b></div>
    </div>
  </div>
  <div class="panel">
    <div class="hero" role="img" aria-label="Close-up photo of a bright smile">
      <div class="hours"><strong>CONVENIENT SATURDAY HOURS!</strong><span>Tue, Thur 9:30am–5:00pm<br>Fri, Sat 9:00am–5:00pm</span></div>
    </div>
    <div class="call">Call us Today<strong>555-214-7080</strong></div>
    <div class="address"><b>ADDRESS</b>270 Harbor Lane<br>Suite 12<br>Eastport, ST 00451</div>
    <div class="map-title">LOCATION MAP</div>
    <div class="map" role="img" aria-label="Street map showing the clinic location"></div>
    <div class="web">www.brightharborclinic.example</div>
  </div>
  <div class="panel">
    <div class="collage-top" role="img" aria-label="Photo collage of smiling mouths"></div>
    <div class="brand-tile"><i></i><span>Bright Harbor Clinic</span></div>
    <div class="collage" role="img" aria-label="Photo collage of happy patient smiles"></div>
    <div class="offer">
      <h2>Special Offer</h2>
      <div class="deal"><div class="price">$69</div><div class="what">New Patients Special</div></div>
      <div class="deal navy"><div class="price">$99</div><div class="what">Attice Teeth Whitening</div></div>
      <p>25% off ClearFit Aligners</p>
    </div>
  </div>
</section>

<div class="row-label" style="top:596px">R2</div>
<section class="sheet" style="top:626px;height:566px">
  <div class="panel">
    <div class="promo">
      <h2 style="margin-bottom:8px">Our Promos</h2>
      <div class="deal"><div class="price">$69</div><div class="what">New Patients Special<br>Exam, Cleaning, Digital X-Rays<small>Regular Price $240</small></div></div>
      <div class="deal navy"><div class="price">$99</div><div class="what">$99 In Office Teeth Whitening<small>Regular Price $700</small></div></div>
      <p class="promo-note">25-40% OFF On ClearFit Aligners<br>Plus Free Consultation</p>
    </div>
    <div class="services">
      <h2>Our Services</h2>
      <div class="svc"><div class="ph" role="img" aria-label="Photo of dental cleaning"></div><span>Clearing &amp; Prevention</span></div>
      <div class="svc"><div class="ph" role="img" aria-label="Photo of cosmetic dentistry"></div><span>Cosmetic Dentistry</span></div>
      <div class="svc"><div class="ph" role="img" aria-label="Photo of removable dentures"></div><span>Removable Dentures</span></div>
      <div class="svc"><div class="ph" role="img" aria-label="Photo of orthodontic braces"></div><span>Orthodontics</span></div>
      <div class="svc"><div class="ph" role="img" aria-label="Photo of a child at the dentist"></div><span>Pediatric Dentistry</span></div>
    </div>
  </div>
  <div class="panel">
    <div class="teeth" role="img" aria-label="Illustration of two cheerful cartoon teeth"></div>
    <ul class="checks">
      <li><svg width="16" height="16" viewBox="0 0 16 16"><circle cx="8" cy="8" r="8" fill="var(--teal)"/><path d="M4 8.5l2.5 2.5L12 5.5" stroke="#fff" stroke-width="2" fill="none"/></svg>Payment Option Available!</li>
      <li><svg width="16" height="16" viewBox="0 0 16 16"><circle cx="8" cy="8" r="8" fill="var(--teal)"/><path d="M4 8.5l2.5 2.5L12 5.5" stroke="#fff" stroke-width="2" fill="none"/></svg>Financing Options Available!</li>
      <li><svg width="16" height="16" viewBox="0 0 16 16"><circle cx="8" cy="8" r="8" fill="var(--teal)"/><path d="M4 8.5l2.5 2.5L12 5.5" stroke="#fff" stroke-width="2" fill="none"/></svg>Most Ambulances Accepted!</li>
      <li><svg width="16" height="16" viewBox="0 0 16 16"><circle cx="8" cy="8" r="8" fill="var(--teal)"/><path d="M4 8.5l2.5 2.5L12 5.5" stroke="#fff" stroke-width="2" fill="none"/></svg>No Insurance?</li>
    </ul>
    <p class="plan">TRY OUR DENTAL<br>SAVINGS PLAN</p>
  </div>
  <div class="panel">
    <div class="tier"><div class="ph" role="img" aria-label="Photo of a preventive dental exam"></div><div class="pct">80%<br>100%<small>Coverage</small></div></div>
    <p class="tier-cap">Preventive Exam · X-Ray Professional Cleaning</p>
    <div class="tier"><div class="ph" role="img" aria-label="Photo of a filling procedure"></div><div class="pct">40%<br>80%<small>Coverage</small></div></div>
    <p class="tier-cap">Filling Crowns Attice Teeth Whitening</p>
    <div class="tier"><div class="ph" role="img" aria-label="Photo of dentures and braces"></div><div class="pct">25%<br>65%<small>Saving</small></div></div>
    <p class="tier-cap">Major Advanced Dentures Extractions Braces Orthodontics</p>
    <div class="fee">Annual Fee<br>$148<br>First Family<br>Member<br>11.5 Month</div>
  </div>
</section>
</body>
</html>
```